Web design for an intellectual property law practice

I need to design a simple landing page that may in the future expand to a full site. It should be very high tech focused.

Target Market(s)

Anyone seeking legal services

Industry/Entity Type

Legal

Number of Pages Required

2 page

Font styles to use
Other font styles liked:
• The same font as my logo

Colors
ec1f27

Requirements
Must have
• My logo (see attached).
Nice to have
• Open to ideas.

```html
<!DOCTYPE html>
<html lang="en">
<head>
<meta charset="utf-8">
<title>Canadian Patent Lawyer</title>
<link href="https://fonts.googleapis.com/css2?family=Roboto:wght@300;400;500;700&display=swap" rel="stylesheet">
<style>
  :root {
    --red: #ec1f27;
    --ink: #1d1d1d;
    --text: #555555;
    --taupe: #d9d0cc;
    --mist: #ececec;
    --paper: #ffffff;
    --soft-btn: #e4e0dd;
    --footer: #1c1c1c;
    --footer-text: #a9a9a9;
  }
  * { margin: 0; padding: 0; box-sizing: border-box; }
  html, body { width: 749px; height: 1200px; overflow: hidden; background: var(--paper); }
  body { font-family: 'Roboto', sans-serif; color: var(--ink); position: relative; }

  .site-header { position: absolute; left: 0; top: 0; width: 749px; height: 102px; background: var(--paper); }
  .brand { position: absolute; left: 0; width: 749px; top: 36px; text-align: center; }
  .brand-mark { display: block; width: 30px; height: 30px; border-radius: 50%; border: 1.5px solid var(--ink); margin: 0 auto 6px; }
  .brand-name { font-size: 12.5px; font-weight: 400; color: var(--ink); letter-spacing: 0.2px; }
  .header-phone { position: absolute; right: 62px; top: 40px; text-align: center; }
  .header-phone svg { display: block; margin: 0 auto 8px; }
  .header-phone span { font-size: 11px; color: var(--red); }

  .hero { position: absolute; left: 0; top: 102px; width: 749px; height: 295px; background: var(--taupe); }
  .hero-title { position: absolute; left: 62px; top: 98px; font-size: 18px; font-weight: 500; letter-spacing: 0.1px; }
  .hero-title em { font-style: normal; color: var(--red); }
  .hero-copy { position: absolute; left: 62px; top: 132px; width: 320px; font-size: 8.5px; line-height: 14px; color: var(--text); }
  .hero-copy strong { color: #333; font-weight: 500; }
  .btn-red { position: absolute; background: var(--red); color: #fff; display: flex; align-items: center; justify-content: center; }
  .hero .btn-red { left: 62px; top: 198px; width: 119px; height: 34px; font-size: 11px; }
  .hero-portrait { position: absolute; left: 452px; top: 10px; width: 236px; height: 285px; background: linear-gradient(180deg, #cfc6c1 0%, #b9aba3 45%, #3c3b40 75%, #2a2a2f 100%); border-radius: 110px 110px 0 0; }

  .about { position: absolute; left: 0; top: 397px; width: 749px; height: 257px; text-align: center; }
  .section-title { font-size: 14px; font-weight: 500; color: var(--ink); }
  .about .section-title { position: absolute; top: 65px; width: 100%; }
  .about-copy { position: absolute; left: 60px; top: 108px; width: 629px; font-size: 9.5px; line-height: 14px; color: var(--text); font-weight: 300; }
  .about .btn-red { left: 333px; top: 183px; width: 92px; height: 24px; font-size: 9.5px; }

  .experience { position: absolute; left: 0; top: 654px; width: 749px; height: 283px; background: var(--mist); }
  .experience-backdrop { position: absolute; left: 260px; top: 16px; width: 440px; height: 267px; background: radial-gradient(ellipse at 50% 55%, #e3e6e6 0%, #e9eaea 55%, var(--mist) 100%); }
  .experience .section-title { position: absolute; top: 24px; width: 100%; text-align: center; }
  .service { position: absolute; top: 61px; width: 190px; height: 222px; text-align: center; }
  .service.is-active { background: var(--taupe); border-top: 3px solid var(--red); }
  .service h3 { position: absolute; top: 30px; left: 0; width: 100%; font-size: 10.5px; font-weight: 400; line-height: 14px; color: #2a2a2a; }
  .service p { position: absolute; top: 74px; left: 14px; width: 162px; font-size: 7px; line-height: 13px; color: var(--text); }
  .service .btn-soft { position: absolute; top: 173px; left: 52px; width: 74px; height: 22px; background: var(--soft-btn); color: var(--red); font-size: 7px; display: flex; align-items: center; justify-content: center; }

  .cta { position: absolute; left: 0; top: 937px; width: 749px; height: 181px; background: #fdfdfd; }
  .cta-title { position: absolute; left: 186px; top: 69px; font-size: 18px; font-weight: 400; }
  .cta-phone { position: absolute; left: 436px; top: 52px; width: 125px; height: 26px; background: var(--red); color: #fff; font-size: 14px; display: flex; align-items: center; justify-content: center; }
  .cta-email { position: absolute; left: 436px; top: 85px; width: 125px; height: 25px; background: var(--ink); color: #fff; font-size: 9px; font-weight: 500; display: flex; align-items: center; justify-content: center; }

  .site-footer { position: absolute; left: 0; top: 1118px; width: 749px; height: 82px; background: var(--footer); }
  .legal { position: absolute; left: 62px; top: 31px; font-size: 8px; line-height: 13px; color: var(--footer-text); }
  .social { position: absolute; right: 73px; top: 34px; display: flex; gap: 6px; }
  .social span { width: 18px; height: 18px; border-radius: 50%; background: #fff; display: block; }
</style>
</head>
<body>
  <header class="site-header">
    <div class="brand">
      <span class="brand-mark"></span>
      <span class="brand-name">northpatentcounsel</span>
    </div>
    <div class="header-phone">
      <svg width="16" height="13" viewBox="0 0 16 13" aria-hidden="true">
        <path d="M1 4 Q8 -1 15 4 L13 6 L11 4.5 L5 4.5 L3 6 Z" fill="#1d1d1d"/>
        <rect x="3" y="6" width="10" height="7" rx="1" fill="#1d1d1d"/>
        <circle cx="8" cy="9.5" r="1.8" fill="#fff"/>
      </svg>
      <span>(416) 555-0142</span>
    </div>
  </header>

  <section class="hero">
    <h1 class="hero-title">CANADIAN PATENT <em>LAWYER</em></h1>
    <p class="hero-copy"><strong>Daniel R. Whitcombe</strong> is a patent lawyer with expertise in the acquisition, protection &amp; enforcement of intellectual property in Canada. Helping you with your Canadian IP rights.</p>
    <a class="btn-red">Contact Me</a>
    <div class="hero-portrait" role="img" aria-label="Portrait photograph of the lawyer in a dark suit and glasses"></div>
  </section>

  <section class="about">
    <h2 class="section-title">About Me</h2>
    <p class="about-copy">DANIEL R. WHITCOMBE is a partner with HARLOW BRIGGS in its Toronto Office.&nbsp; Daniel is an intellectual property lawyer with the firm's Technology and Intellectual Property practice groups. Daniel's practice focuses on all aspects of the acquisition, protection, enforcement and strategic use of a wide range of intellectual property assets in Canada and around the world.</p>
    <a class="btn-red">Read More</a>
  </section>

  <section class="experience">
    <div class="experience-backdrop" role="img" aria-label="Faint background of patent technical drawings and IP category tiles"></div>
    <h2 class="section-title">Experience</h2>
    <article class="service is-active" style="left:62px;">
      <h3>Patents &amp; Industrial Designs</h3>
      <p>As a registered patent agent with the Canadian Intellectual Property Office (CIPO), Daniel's practice focuses on the drafting and prosecuting of patent applications in</p>
      <a class="btn-soft">Read More</a>
    </article>
    <article class="service" style="left:280px;">
      <h3>Patents &amp; Industrial Designs</h3>
      <p>As a registered patent agent with the Canadian Intellectual Property Office (CIPO), Daniel's practice focuses on the drafting and prosecuting of patent applications in</p>
      <a class="btn-soft">Read More</a>
    </article>
    <article class="service" style="left:502px;">
      <h3>Commercial Intellectual Property &amp; Commercialization of IP</h3>
      <p>As a registered patent agent with the Canadian Intellectual Property Office (CIPO), Daniel's practice focuses on the drafting and prosecuting of patent applications in</p>
      <a class="btn-soft">Read More</a>
    </article>
  </section>

  <section class="cta">
    <h2 class="cta-title">Canadian Patent Lawyer</h2>
    <a class="cta-phone">(416) 555-0142</a>
    <a class="cta-email">SEND ME AN EMAIL</a>
  </section>

  <footer class="site-footer">
    <p class="legal">Copyright © 2018<br>Daniel R. Whitcombe&nbsp; - All Rights Reserved.</p>
    <nav class="social" aria-label="Social profiles">
      <span></span><span></span><span></span><span></span>
    </nav>
  </footer>
</body>
</html>
```